Verodex business card

Business card for sustainable investment company called "Verodex". Verodex is an exchange platform selling carbon credits between buyers and sellers. Carbon Credits are an environmental commodity for reducing global carbon emissions.

the card should obviously have our logo and the theme should be sustainability/environment mixed with a trading platform.

Contact Information for Business Card

Logo, Name, Title, Phone, Email

Colors
0054AA
0677BA
7BADD7
CADEEF
E8F1F8
0094D4
00A9DD
6FCCEA
C7EBF8
E9F6FB
00AB8E
00BBA5
67D7C9
C6EFE9
E9F9F6
59FF00
82FF00
B8FF75
E3FFCB
F4FFEA

```html
<!DOCTYPE html>
<html lang="en">
<head>
<meta charset="utf-8">
<title>Verodex Business Card</title>
<link rel="stylesheet" href="https://fonts.googleapis.com/css2?family=Montserrat:wght@400;500;600;700&display=swap">
<style>
  :root{
    --navy:#172a52;
    --sky:#55a6d3;
    --ink:#1e2a3a;
    --paper:#ffffff;
    --stage:#e6e8eb;
  }
  *{margin:0;padding:0;box-sizing:border-box;}
  html,body{width:1200px;height:1059px;overflow:hidden;background:var(--stage);}
  body{position:relative;font-family:'Montserrat',sans-serif;}
  .card{position:absolute;border-radius:18px;overflow:hidden;}
  .card-front{left:256px;top:100px;width:688px;height:391px;background:var(--paper);}
  .card-back{left:253px;top:537px;width:694px;height:394px;background:var(--navy);}
  .wave{position:absolute;left:0;top:0;width:688px;height:391px;}
  .brand{position:absolute;display:flex;align-items:center;}
  .brand-front{left:35px;top:150px;gap:14px;}
  .brand-mark{background:var(--sky);border-radius:4px;}
  .brand-front .brand-mark{width:44px;height:44px;}
  .brand-name{font-weight:600;letter-spacing:0.5px;line-height:1;}
  .brand-front .brand-name{font-size:40px;color:var(--navy);}
  .divider{position:absolute;left:343px;top:74px;width:2px;height:204px;background:var(--sky);}
  .details{position:absolute;left:374px;top:72px;color:var(--ink);}
  .person-name{font-size:26px;font-weight:700;color:var(--navy);letter-spacing:0.8px;line-height:1.05;}
  .person-title{font-size:17px;font-weight:500;letter-spacing:0.6px;margin-top:1px;}
  .address{font-size:15.5px;line-height:22px;margin-top:22px;letter-spacing:0.3px;}
  .contacts{list-style:none;margin-top:18px;}
  .contacts li{display:flex;align-items:center;gap:9px;font-size:16px;height:26px;letter-spacing:0.3px;}
  .contacts svg{width:12px;height:12px;flex:none;}
  .brand-back{left:50%;top:50%;transform:translate(-50%,-50%);gap:22px;}
  .brand-back .brand-mark{width:72px;height:72px;border-radius:6px;}
  .brand-back .brand-name{font-size:66px;color:var(--paper);}
</style>
</head>
<body>
  <section class="card card-front">
    <svg class="wave" viewBox="0 0 688 391" aria-hidden="true">
      <path d="M0,312 C110,372 260,372 420,340 C520,320 590,300 635,306 C662,310 678,322 688,332 L688,391 L0,391Z" fill="#55a6d3"/>
      <path d="M0,316 C110,374 260,374 420,346 C530,326 600,316 645,322 C666,326 680,334 688,342 L688,391 L0,391Z" fill="#ffffff"/>
      <path d="M0,319 C110,377 260,377 420,350 C530,330 600,320 645,326 C666,330 680,338 688,346 L688,391 L0,391Z" fill="#172a52"/>
    </svg>
    <div class="brand brand-front">
      <span class="brand-mark"></span>
      <span class="brand-name">VERODEX</span>
    </div>
    <div class="divider"></div>
    <div class="details">
      <h1 class="person-name">DANIEL REYES</h1>
      <p class="person-title">MANAGER</p>
      <p class="address">2715 Harbor Ridge Rd. Suite 410<br>Lakemont, OR 97124</p>
      <ul class="contacts">
        <li><svg viewBox="0 0 12 12"><path d="M2.5 1 L4.5 1 L5.3 3.4 L4 4.4 C4.6 5.8 6.2 7.4 7.6 8 L8.6 6.7 L11 7.5 L11 9.5 C11 10.3 10.3 11 9.5 11 C5 11 1 7 1 2.5 C1 1.7 1.7 1 2.5 1Z" fill="#55a6d3"/></svg>555-204-3187</li>
        <li><svg viewBox="0 0 12 12"><rect x="0.5" y="2" width="11" height="8" rx="1" fill="#55a6d3"/><path d="M0.8 2.6 L6 6.6 L11.2 2.6" fill="none" stroke="#fff" stroke-width="1"/></svg>hello@verodexmail.com</li>
        <li><svg viewBox="0 0 12 12" fill="none" stroke="#55a6d3" stroke-width="0.9"><circle cx="6" cy="6" r="5.2"/><ellipse cx="6" cy="6" rx="2.3" ry="5.2"/><path d="M0.8 6 H11.2 M1.6 3.4 H10.4 M1.6 8.6 H10.4"/></svg>www.verodexmarkets.com</li>
      </ul>
    </div>
  </section>

  <section class="card card-back">
    <div class="brand brand-back">
      <span class="brand-mark"></span>
      <span class="brand-name">VERODEX</span>
    </div>
  </section>
</body>
</html>
```